Website Banner Redesign for Kelbra Gearbin Centre

Business Name:
KELBRA GEARBIN CENTRE

About Us:
- We’re a proudly Australian company that designs and builds tough, reliable toolboxes for Utes, Trucks, and Campervans. Our products are made to handle harsh conditions and are trusted by tradies, off-roaders, and professional fleets across the country.

Project Goal:
- We want to refresh our homepage and category banners with bold, modern designs that better showcase our products and value proposition.

Why We’re Updating:
Our current banners show the products well, but we want to improve:
Visual impact and hierarchy
- Readability of text (especially on mobile)
- Clearer calls-to-action (CTAs)
- Brand messaging around “Built Tough”, “Aussie Made”, and “Custom Fit-Outs”

Target Audience:
- Tradespeople
- 4x4 & off-road enthusiasts
- Caravan & camping community
- Ute/Truck/Caravan dealerships
- Fleet and commercial buyers

Design Style We Want:
- Bold, confident, rugged
- Clean layout with clear focal points
- Strong product imagery (we’ll supply photos)
- Use of brand colors: Black, White, Red, Grey
- Professional, not too busy or cluttered

Banner Uses:
- Homepage hero banner
- Category landing pages

UTE TOOLBOXES - https://www.kelbragearbin.com.au/aluminium-toolboxes/
Truck Boxes - https://www.kelbragearbin.com.au/truck-toolboxes/
Canopies - https://www.kelbragearbin.com.au/canopy/
Dog Boxes - https://www.kelbragearbin.com.au/dog-boxes/
CAMPER BOXES - https://www.kelbragearbin.com.au/camper-toolboxes/
Accessories - https://www.kelbragearbin.com.au/accessories/

- Can be reused for desktop and mobile

Inspiration Style:
Think: 4x4 accessory brands, tough tradie gear, or clean eCommerce landing banners from premium auto suppliers.

Target Market(s)

All in Brief Above

Industry/Entity Type

Retail

Requirements
Must have
• A banner using our products only. A banner for each category, and 2 alternate banners for the home page.
Nice to have
• I have added some designs which i like..... Please take a look and take inspiration from them.

```html
<!DOCTYPE html>
<html lang="en">
<head>
<meta charset="utf-8">
<title>Kelbra Gearbin Centre – Campervan Boxes Banner</title>
<link rel="stylesheet" href="https://fonts.googleapis.com/css2?family=Anton&family=Open+Sans:ital,wght@0,400;0,600;0,700;1,400&family=Poppins:wght@500;700&display=swap">
<style>
  :root{
    --board:#4d4d4d;
    --black:#000;
    --ink:#1b1b1b;
    --white:#fff;
    --red:#a11d4a;
    --red-dark:#7c1236;
    --yellow:#f7d000;
    --text:#333;
  }
  *{box-sizing:border-box;margin:0;padding:0}
  html,body{width:1200px;height:1200px;overflow:hidden}
  body{background:var(--board);position:relative;font-family:"Open Sans",sans-serif;color:var(--text)}

  /* ---------- banner ---------- */
  .banner{position:absolute;width:1042px;height:292px;overflow:hidden;background:var(--black)}
  .banner-backdrop{position:absolute;inset:0;
    background:radial-gradient(ellipse at 55% 45%,#f2f2f2 0%,#cfcfcf 45%,#707070 78%,#1a1a1a 100%)}
  .banner-products{position:absolute;left:170px;top:55px;width:645px;height:235px;border-radius:6px;
    background:linear-gradient(90deg,
      rgba(250,250,250,0) 0%,#f6f6f6 4%,#e4e4e4 18%,#cfcfcf 23%,
      #262626 27%,#0e0e0e 40%,#2b2b2b 52%,
      #d9d9d9 56%,#bdbdbd 70%,#e8e8e8 88%,#f1f1f1 96%,rgba(240,240,240,0) 100%);
    box-shadow:0 14px 22px -10px rgba(0,0,0,.45)}
  .banner-frame{position:absolute;top:0;bottom:0;width:52px;
    background:linear-gradient(90deg,#050505,#2a2a2a 60%,#bdbdbd 70%,#1a1a1a 78%,#000)}
  .banner-frame.left{left:0}
  .banner-frame.right{right:0;transform:scaleX(-1)}
  .banner-label{position:absolute;left:49px;top:203px;width:222px;height:84px;background:var(--black);
    clip-path:polygon(0 0,82% 0,100% 100%,0 100%)}
  .banner-title{position:absolute;left:80px;top:208px;font-family:"Anton",sans-serif;font-weight:400;
    font-size:33px;line-height:37px;color:var(--white);letter-spacing:.5px;text-transform:uppercase}
  .banner-cta{position:absolute;left:839px;top:226px;width:131px;height:37px;border-radius:19px;
    background:var(--red);border:2px solid var(--red-dark);color:var(--white);
    font-family:"Anton",sans-serif;font-size:26px;line-height:33px;text-align:center}

  /* ---------- website preview ---------- */
  .site{position:absolute;left:79px;top:537px;width:1042px;height:526px;overflow:hidden;background:var(--white)}
  .site-header{position:absolute;left:0;top:0;width:100%;height:41px;background:var(--black)}
  .site-brand{position:absolute;left:210px;top:5px;width:115px;height:31px;border:1px solid var(--white);
    border-radius:3px;color:var(--white);font-family:"Poppins",sans-serif;font-weight:700;
    font-size:9px;line-height:11px;display:flex;align-items:center;justify-content:center;text-align:center}
  .site-search{position:absolute;left:487px;top:11px;width:234px;height:20px;background:var(--white);
    border-radius:3px;font-size:7px;color:#999;padding:5px 10px}
  .site-search svg{position:absolute;right:8px;top:5px}
  .site-cart{position:absolute;left:733px;top:15px;font-size:8px;color:var(--white);font-family:"Poppins",sans-serif}
  .site-nav{position:absolute;left:0;top:41px;width:100%;height:33px;background:var(--red)}
  .nav-category{position:absolute;left:196px;top:0;width:147px;height:33px;background:var(--yellow);
    font-family:"Poppins",sans-serif;font-weight:500;font-size:8px;color:var(--ink);padding:12px 11px}
  .nav-category .burger{position:absolute;right:11px;top:12px;width:9px}
  .nav-category .burger i{display:block;height:1.5px;background:var(--ink);margin-bottom:2px}
  .nav-links{position:absolute;left:359px;top:12px;display:flex;gap:9px;font-family:"Poppins",sans-serif;
    font-size:7.5px;color:var(--white)}
  .nav-util{position:absolute;top:12px;font-family:"Poppins",sans-serif;font-size:7.5px;color:var(--white)}
  .site .banner{left:0;top:74px}

  .intro{position:absolute;left:0;top:380px;width:100%;text-align:center}
  .intro h2{font-family:"Poppins",sans-serif;font-weight:700;font-size:14px;letter-spacing:1px;color:var(--black)}
  .intro p{font-size:7px;line-height:11.5px;color:var(--text);width:620px;margin:4px auto 0}
  .intro p.quote{font-style:italic;margin-top:6px}
  .intro a{color:var(--red);font-weight:700;text-decoration:none}
  .collection-title{position:absolute;left:0;top:479px;width:100%;text-align:center;
    font-family:"Poppins",sans-serif;font-weight:700;font-size:11px;letter-spacing:1px;color:var(--black)}
  .collection-rule{position:absolute;left:205px;top:497px;width:633px;height:1px;background:#ddd}
  .collection-tab{position:absolute;top:508px;height:30px;background:var(--black);border-radius:3px 3px 0 0;
    color:var(--white);font-family:"Poppins",sans-serif;font-weight:500;font-size:8px;text-align:center;padding-top:9px}

  .review-badge{position:absolute;left:0;top:484px;width:112px;height:37px;background:var(--white);
    border-top:2px solid #3cba54;font-size:7px;padding:4px 0 0 28px;line-height:10px}
  .review-badge .mark{position:absolute;left:3px;top:10px;width:19px;height:19px;border-radius:50%;border:2px solid #e8a200}
  .review-badge .score{color:#e37400;font-size:9px}
  .chat-bubble{position:absolute;left:871px;top:418px;width:157px;height:53px;background:var(--white);
    border-radius:5px;box-shadow:0 1px 6px rgba(0,0,0,.2);font-size:7.5px;line-height:12px;padding:12px 10px 0 45px;color:var(--ink)}
  .chat-bubble .avatar{position:absolute;left:14px;top:13px;width:23px;height:23px;border-radius:50%;background:var(--red)}
  .text-us{position:absolute;left:960px;top:485px;width:67px;height:24px;border-radius:12px;background:var(--red);
    color:var(--white);font-family:"Poppins",sans-serif;font-weight:700;font-size:8px;padding:6px 0 0 27px}
  .text-us::before{content:"";position:absolute;left:10px;top:7px;width:11px;height:9px;border-radius:4px;background:var(--white)}
</style>
</head>
<body>

  <section class="banner" style="left:79px;top:131px">
    <div class="banner-backdrop"></div>
    <div class="banner-products" role="img" aria-label="Product photo: white, black and polished aluminium campervan toolboxes with gullwing lids open"></div>
    <div class="banner-frame left"></div>
    <div class="banner-frame right"></div>
    <div class="banner-label"></div>
    <h1 class="banner-title">Campervan<br>Boxes</h1>
    <div class="banner-cta">CLICK HERE</div>
  </section>

  <section class="site">
    <header class="site-header">
      <div class="site-brand">KELBRA GEARBIN<br>CENTRE</div>
      <div class="site-search">Search...
        <svg width="10" height="10" viewBox="0 0 10 10"><circle cx="4" cy="4" r="3" fill="none" stroke="#a11d4a" stroke-width="1.2"/><line x1="6.2" y1="6.2" x2="9" y2="9" stroke="#a11d4a" stroke-width="1.2"/></svg>
      </div>
      <div class="site-cart">
        <svg width="14" height="10" viewBox="0 0 14 10" style="vertical-align:-2px"><path d="M0 1h3l2 6h7l1-4H4" fill="none" stroke="#fff" stroke-width="1"/><circle cx="6" cy="9" r="1" fill="#fff"/><circle cx="11" cy="9" r="1" fill="#fff"/></svg>
        MY CART &nbsp; $0.00 ▾
      </div>
    </header>
    <nav class="site-nav">
      <div class="nav-category">Shop By Category<span class="burger"><i></i><i></i><i></i></span></div>
      <div class="nav-links"><span>PRODUCTS</span><span>ABOUT US</span><span>CONTACT US</span><span>SALE</span></div>
      <div class="nav-util" style="left:628px">☎ 1300 KEL BIN</div>
      <div class="nav-util" style="left:706px">♡ Wishlists</div>
      <div class="nav-util" style="left:767px">○ Login &nbsp;|&nbsp; Register</div>
    </nav>

    <section class="banner">
      <div class="banner-backdrop"></div>
      <div class="banner-products" role="img" aria-label="Product photo: white, black and polished aluminium campervan toolboxes with gullwing lids open"></div>
      <div class="banner-frame left"></div>
      <div class="banner-frame right"></div>
      <div class="banner-label"></div>
      <h2 class="banner-title">Campervan<br>Boxes</h2>
      <div class="banner-cta">CLICK HERE</div>
    </section>

    <div class="intro">
      <h2>TOOLBOXES FOR UTES</h2>
      <p class="quote">"Kelbra Gearbin has one of the largest and most comprehensive range of premium aluminium flat plate toolboxes for utes in Australia."</p>
      <p>Our ute toolboxes come in a wide range of sizes and multiple configurations that can be fitted onto any ute or truck.</p>
      <p>At present, we provide ute toolboxes, aluminium gullwing canopy for ute, truck toolboxes, dog boxes, trailer toolboxes, and other ute and truck aluminium toolboxes to our customers. Shop with us and promote local businesses online. If you have any suggestions you think can improve our toolbox business, please feel free to <a>call</a> or <a>write</a> to the Kelbra team.</p>
    </div>
    <div class="collection-title">OUR COLLECTION</div>
    <div class="collection-rule"></div>
    <div class="collection-tab" style="left:201px;width:153px">White Pro Series</div>
    <div class="collection-tab" style="left:363px;width:154px">Black Pro Series</div>
    <div class="collection-tab" style="left:527px;width:152px">Full Lid Toolboxes</div>
    <div class="collection-tab" style="left:689px;width:154px">Half Lid Toolboxes</div>

    <div class="review-badge"><span class="mark"></span>Kelbra Gearbin Centre<br><span class="score">5.0 ★★★★★</span><br>powered by Revora</div>
    <div class="chat-bubble"><span class="avatar"></span>Have a question? Chat with us here.</div>
    <div class="text-us">Text us</div>
  </section>

</body>
</html>
```